Firma für Temperaturmessung und Temperaturkalibrierung sucht Broschürendesign
Zielgruppe
Wir sind eine Firma für Temperaturmessung und Temperaturkalibrierung. Unsere Zielgruppe sind Unternehmen aus Industrie, Forschung & Entwicklung. Entsprechend suchen wir ein Design, das professionell unsere Produkte und Dienstleistungen repräsentiert.
Aufgabenstellung
Mögliche Maße sind:
DIN A6 = 10,5 x 14,8 cm
DIN B6 = 12,5 x 17,6 cm
DIN C6 = 11,4 x 16,2 cm
DIN D6 = 9,6 x 13,6 cm
Zur Orientierung des Designs sehen Sie folgende Webseiten:
https://www.termivo-mess.de/en/manufaktur/
https://www.termivo-mess.de/en/technologie/
Den Text sowie die Bilder, die zu verwenden sind, finden Sie in der unten stehenden Datei.

```html
<!DOCTYPE html>
<html lang="en">
<head>
<meta charset="utf-8">
<title>Termivo Manufacture Brochure</title>
<link href="https://fonts.googleapis.com/css2?family=Open+Sans:wght@400;600;700&display=swap" rel="stylesheet">
<style>
:root{
  --backdrop:#ece8e3;
  --paper:#ffffff;
  --panel:#f0f0f0;
  --page-grey:#e9e9ea;
  --ink:#3a3a3a;
  --ink-soft:#555;
  --accent:#b5322c;
  --accent-dark:#9e2a25;
  --photo-lab:linear-gradient(160deg,#e6e6e8 0%,#cfd2d6 45%,#b9a79a 100%);
  --photo-warm:linear-gradient(145deg,#9a8a78,#c9a27a 55%,#6d6256);
  --photo-cool:linear-gradient(145deg,#d8dadf,#9aa0aa 60%,#6a7280);
  --photo-dark:linear-gradient(150deg,#2e3440,#4a5566 60%,#22262d);
  --photo-print:linear-gradient(120deg,#d9dbe3,#a7adc0 45%,#c7474a 75%,#eee);
  --photo-portrait:linear-gradient(160deg,#c23b36,#d9d5d2 60%,#8f8a86);
}
*{box-sizing:border-box;margin:0;padding:0}
html,body{width:1200px;height:1048px;overflow:hidden}
body{background:var(--backdrop);font-family:"Open Sans",Arial,sans-serif;color:var(--ink);position:relative}

.spread,.cover{position:absolute;background:var(--page-grey);box-shadow:0 2px 6px rgba(0,0,0,.12);overflow:hidden}
.spread::after{content:"";position:absolute;top:0;bottom:0;left:50%;width:14px;margin-left:-7px;background:linear-gradient(90deg,rgba(0,0,0,0),rgba(0,0,0,.12),rgba(0,0,0,0));pointer-events:none}
.spread--manufacture{left:470px;top:76px;width:565px;height:388px}
.spread--technology{left:127px;top:530px;width:560px;height:390px}
.cover{left:773px;top:524px;width:275px;height:388px;background:var(--paper)}

.photo{position:absolute}
.lab{background:var(--photo-lab)}
.warm{background:var(--photo-warm)}
.cool{background:var(--photo-cool)}
.dark{background:var(--photo-dark)}
.print{background:var(--photo-print)}
.portrait{background:var(--photo-portrait)}
.drawing{background:linear-gradient(180deg,#fafafa,#eee)}

.box{position:absolute;background:var(--paper);padding:10px 12px}
.box--grey{background:var(--panel)}
.title{font-size:12px;font-weight:700;line-height:1.15;letter-spacing:.3px;text-transform:uppercase;margin-bottom:7px;color:#333}
p,li{font-size:6.6px;line-height:1.55;color:var(--ink-soft)}
.intro p{font-size:6.3px;line-height:1.5}
.brand{color:var(--accent);font-weight:700}
.item{position:absolute;display:flex;gap:12px}
.item .photo{position:static;flex:0 0 auto}
.item h3{font-size:7.6px;font-weight:700;line-height:1.25;margin:8px 0 6px;color:#333}
.item p{text-align:justify}

.bullets{list-style:none;position:absolute}
.bullets li{font-weight:600;color:#333;padding-left:8px;position:relative}
.bullets li::before{content:"";position:absolute;left:0;top:3px;width:3px;height:3px;border-radius:50%;background:#333}

.contact h4{font-size:8.4px;font-weight:400;line-height:1.3;color:#444;margin:12px 0 8px}
.contact p{font-size:6.6px}

.cover-brand{position:absolute;font-size:13px;font-weight:600;color:#555;letter-spacing:.3px}
.company{position:absolute;left:26px;top:194px;display:flex;align-items:center;gap:8px}
.company .mark{width:30px;height:24px;border:1px solid var(--accent)}
.company span{font-size:8px;font-weight:700;color:#333}
.address{position:absolute;left:26px;font-size:6.6px;line-height:1.45;color:#333}
.url-bar{position:absolute;right:22px;bottom:16px;width:83px;height:26px;background:var(--accent-dark);color:#fff;font-size:6.6px;display:flex;align-items:center;justify-content:center}
</style>
</head>
<body>

<section class="spread spread--manufacture">
  <div class="photo lab" style="left:0;top:0;width:565px;height:165px" role="img" aria-label="Photo of the bright manufacturing lab with workbenches and wire spools"></div>

  <div class="box intro" style="left:20px;top:46px;width:252px;height:136px">
    <h1 class="title">Precision thermometers<br>handmade</h1>
    <p>In the <span class="brand">Termivo</span> manufacture of Brundtwerk the precision thermometers are manufactured by careful manual work in Hollerbach/Germany. In addition to the construction of the actual thermometers, a further focus is the development of our own tools and production processes. For design, production and final accredited calibration, no external suppliers are required apart from the raw materials. This independence ensures the high quality of the thermometers.</p>
  </div>

  <div class="item" style="left:42px;top:190px;width:212px">
    <div class="photo cool" style="width:74px;height:70px" role="img" aria-label="Photo of a technician machining parts on a lathe"></div>
    <div><h3>Mechanical production</h3><p>Required components, such as handles or prototypes for further development, are manufactured by machining.</p></div>
  </div>

  <div class="item" style="left:42px;top:280px;width:212px">
    <div class="photo warm" style="width:74px;height:70px" role="img" aria-label="Photo of thermocouple wire during heat treatment"></div>
    <div><h3>Thermal treatment of<br>thermal material</h3><p>A core competence is the targeted thermal treatment of thermowires. Our aging processes ensure a metallurgically stable and thermoelectrically homogeneous condition of the <span class="brand">Termivo</span> thermocouples.</p></div>
  </div>

  <div class="box box--grey" style="left:290px;top:72px;width:245px;height:298px"></div>

  <div class="item" style="left:298px;top:82px;width:232px">
    <div class="photo cool" style="width:70px;height:72px" role="img" aria-label="Photo of a welding flame at a noble metal wire"></div>
    <div><h3>Noble metal welding process</h3><p>Thermocouple wires and connecting cables are welded together precisely by hand. The required fuel gases hydrogen and oxygen are not stored in bottles, but are produced in a 2:1 mixture ratio of water by electrolysis. This guarantees the purity of the fuel gas.</p></div>
  </div>

  <div class="item" style="left:298px;top:180px;width:232px">
    <div class="photo cool" style="width:70px;height:72px" role="img" aria-label="Photo of laser welding under a microscope"></div>
    <div><h3>Laser Welding</h3><p>Particularly filigree connections, such as the connecting wires of the temperature detector, are welded under the microscope with precision lasers.</p></div>
  </div>

  <div class="item" style="left:298px;top:276px;width:232px">
    <div class="photo dark" style="width:70px;height:72px" role="img" aria-label="Photo of the annealing furnace control panel"></div>
    <div><h3>Annealing of resistance<br>thermometers</h3><p>Resistance thermometers are completely annealed according to our adapted annealing cycles in a specially designed annealing furnace with oxygen circulation.</p></div>
  </div>
</section>

<section class="spread spread--technology">
  <div class="photo print" style="left:0;top:0;width:560px;height:180px" role="img" aria-label="Close-up photo of a 3D printer producing handle parts"></div>

  <div class="box" style="left:22px;top:14px;width:248px;height:162px;padding:10px 12px 0 16px">
    <div class="photo portrait" style="position:static;float:left;width:74px;height:72px;margin:10px 10px 4px 0" role="img" aria-label="Photo of a printed thermometer handle"></div>
    <h3 style="font-size:7.6px;font-weight:700;margin:6px 0 5px;color:#333">3D printing</h3>
    <p>Insulation elements and complex plastic parts inside the handles, such as strain reliefs, are manufactured using a modern 3D printing process. This offers us many advantages. Complex designs are produced without manual detours and without expensive tools. This saves a lot of time and money. By means of 3D printing, <span class="brand" style="color:#333">Termivo</span> thermometers can be manufactured as a modular system according to customer specifications.</p>
  </div>

  <div class="photo drawing" style="left:34px;top:186px;width:84px;height:146px" role="img" aria-label="Technical drawing of a thermocouple probe in the inhomogeneity scanner"></div>

  <div style="position:absolute;left:128px;top:190px;width:130px">
    <h3 style="font-size:7.6px;font-weight:700;margin-bottom:5px;color:#333">Inhomogeneity Scanner</h3>
    <p style="text-align:justify">Possible inhomogeneities of the <span class="brand">Termivo</span> thermocouples are examined with the help of an inhomogeneity scanner. A mobile heat source tests the entire thermal material of the measuring point for local inhomogeneities. The inhomogeneity scanner is a proprietary development of the <span class="brand">Brundtwerk company</span>. With it the thermocouples of the <span class="brand">Termivo</span> manufacture can be improved substantially:</p>
  </div>

  <ul class="bullets" style="left:38px;top:336px">
    <li>More realistic consideration of the measurement uncertainties</li>
    <li>Checking the thermal treatment</li>
    <li>Improvement of quality and manufacturing processes</li>
  </ul>

  <div class="box box--grey" style="left:282px;top:192px;width:250px;height:178px"></div>

  <div class="item contact" style="left:292px;top:204px">
    <div class="photo portrait" style="width:62px;height:66px" role="img" aria-label="Portrait photo of contact person Ina Vollrath"></div>
    <div><h4>Questions about Termivo<br>Manufacture?</h4><p>Contact person:&nbsp;&nbsp; Ina Vollrath<br>i.vollrath@brundtwerk.com</p></div>
  </div>

  <div class="item contact" style="left:292px;top:288px">
    <div class="photo portrait" style="width:62px;height:66px" role="img" aria-label="Portrait photo of contact person Jonas Harder"></div>
    <div><h4>Questions about the<br>technology?</h4><p>Contact person:&nbsp;&nbsp; Jonas Harder<br>jonas.harder@brundtwerk.com</p></div>
  </div>
</section>

<section class="cover">
  <div class="cover-brand" style="left:14px;top:10px">Termivo</div>
  <div class="photo lab" style="left:0;top:30px;width:275px;height:146px" role="img" aria-label="Photo of the manufacturing lab with workbenches and chairs"></div>

  <div class="company"><div class="mark"></div><span>Brundtwerk</span></div>

  <div class="address" style="top:232px">Brundtwerk<br>Thermometrie- und Prüfbau GmbH</div>
  <div class="address" style="top:264px">Lindenweg 8<br>57412 Hollerbach</div>
  <div class="address" style="top:296px">Tel.:&nbsp; +49 2718 774 20-0<br>Fax.: +49 2718 774 20-10</div>
  <div class="address" style="top:322px">info@brundtwerk.com<br>www.brundtwerk.com</div>

  <div class="cover-brand" style="right:24px;top:318px">Termivo</div>
  <div class="url-bar">www.termivo-mess.de</div>
</section>

</body>
</html>
```